Instagram Posts and promotion

Hi, I am looking for someone to create professional Instagram posts for my new Instagram account about twice a week and help me grow local, organic followers.
The images and posts need to be original and high quality and affordable.
He/she will be given relevant medical topics and sometimes the link to a medical article and should be able to come up with good content.
It is for @kovtahmclinic specializing in Radiofrequency Ablation (RFA) of thyroid nodules.

```html
<!DOCTYPE html>
<html lang="en">
<head>
<meta charset="utf-8">
<title>Kovtahm RFA Clinic – We Care About Your Health</title>
<link rel="stylesheet" href="https://fonts.googleapis.com/css2?family=Arimo:wght@700&family=Lato:wght@400;700&display=swap">
<style>
  :root {
    --navy: #1b5481;
    --teal: #24807f;
    --ink: #2e3440;
    --muted: #8b9099;
    --icon: #3d8fda;
    --icon-light: #8fc4ee;
    --gold: #fbbd5b;
    --white: #ffffff;
    --brand: #c9dde9;
  }
  * { margin: 0; padding: 0; box-sizing: border-box; }
  html, body { width: 1200px; height: 1200px; overflow: hidden; background: var(--white); }
  .post { position: relative; width: 1200px; height: 1200px; overflow: hidden; background: var(--white); font-family: "Lato", sans-serif; }
  .backdrop { position: absolute; inset: 0; }
  .headline-band {
    position: absolute; left: 64px; top: 64px; width: 760px; height: 232px;
    background: var(--teal); border-radius: 60px 0 0 60px;
  }
  .headline {
    position: absolute; left: 153px; top: 88px;
    font-family: "Arimo", sans-serif; font-weight: 700; font-size: 71px; line-height: 86px;
    color: var(--white);
  }
  .brand {
    position: absolute; left: 900px; top: 92px; width: 250px;
    font-family: "Lato", sans-serif; font-weight: 700; font-size: 38px; line-height: 44px;
    color: var(--brand); text-align: center; letter-spacing: 1px;
  }
  .doctor-photo {
    position: absolute; left: 752px; top: 400px; width: 406px; height: 800px;
    border-radius: 203px 203px 0 0;
    background: linear-gradient(180deg, #e9d6c3 0%, #f3f4f6 30%, #dfe7ef 70%, #c8d6e4 100%);
  }
  .features { position: absolute; left: 157px; top: 352px; list-style: none; }
  .feature { display: flex; gap: 26px; height: 152px; }
  .feature svg { width: 80px; height: 80px; flex: none; margin-top: 4px; }
  .feature-title { font-weight: 700; font-size: 25px; color: var(--ink); line-height: 34px; margin-top: 4px; }
  .feature-text { font-size: 25px; color: var(--muted); line-height: 35px; margin-top: 4px; }
  .book-btn {
    position: absolute; left: 157px; top: 816px; width: 179px; height: 53px;
    background: var(--gold); border-radius: 27px; color: var(--white);
    font-weight: 700; font-size: 18px; letter-spacing: 1.5px;
    display: flex; align-items: center; justify-content: center; gap: 12px;
  }
  .call { position: absolute; left: 370px; top: 815px; display: flex; gap: 12px; }
  .call svg { width: 36px; height: 36px; margin-top: 4px; }
  .call-label { font-weight: 700; font-size: 19px; color: var(--ink); line-height: 26px; }
  .call-number { font-size: 19px; color: var(--muted); line-height: 28px; }
  .contact { position: absolute; top: 1133px; display: flex; align-items: center; gap: 14px; color: var(--white); font-size: 19px; }
  .contact svg { width: 30px; height: 24px; }
  .contact-email { left: 69px; }
  .contact-web { left: 432px; }
  .deco { position: absolute; fill: none; stroke: var(--icon-light); stroke-width: 2.5; stroke-linecap: round; stroke-linejoin: round; }
</style>
</head>
<body>
<main class="post">
  <svg class="backdrop" width="1200" height="1200" viewBox="0 0 1200 1200" aria-hidden="true">
    <path fill="var(--navy)" d="M860 0 H1200 V1200 H0 V985 C120 930 260 915 420 950 C560 985 700 1000 800 940 C870 890 880 780 880 680 C880 600 820 560 790 480 C760 400 745 330 748 250 C752 120 790 40 860 0 Z"/>
  </svg>

  <div class="headline-band"></div>
  <h1 class="headline">We Care About<br>Your Health</h1>

  <div class="brand">KOVTAHM<br>RFA CLINIC</div>

  <div class="doctor-photo" role="img" aria-label="Photo of a smiling female doctor in a white coat with a stethoscope, gesturing toward the service list"></div>

  <svg class="deco" style="left:780px;top:318px" width="76" height="76" viewBox="0 0 76 76" aria-hidden="true">
    <rect x="6" y="8" width="64" height="8" rx="2"/><path d="M14 16 V60 a6 6 0 0 0 12 0 V16 M32 16 V60 a6 6 0 0 0 12 0 V16 M50 16 V60 a6 6 0 0 0 12 0 V16 M14 40 H26 M32 36 H44 M50 44 H62"/>
  </svg>
  <svg class="deco" style="left:1060px;top:312px" width="76" height="86" viewBox="0 0 76 86" aria-hidden="true">
    <rect x="8" y="10" width="60" height="72" rx="4"/><rect x="26" y="4" width="24" height="12" rx="3"/><path d="M38 26 V42 M30 34 H46 M20 54 H56 M20 64 H56 M20 74 H44"/>
  </svg>
  <svg class="deco" style="left:205px;top:1005px" width="70" height="70" viewBox="0 0 70 70" aria-hidden="true">
    <path d="M8 44 L24 58 H50 L62 46 M35 10 C28 10 24 16 24 22 C24 32 35 40 35 40 C35 40 46 32 46 22 C46 16 42 10 35 10 Z"/>
  </svg>
  <svg class="deco" style="left:405px;top:985px" width="64" height="76" viewBox="0 0 64 76" aria-hidden="true">
    <path d="M8 6 V70 M8 6 H56 M22 14 H42 V44 H22 Z M32 44 V56 M32 56 C32 66 44 66 44 70"/>
  </svg>
  <svg class="deco" style="left:588px;top:1005px" width="74" height="74" viewBox="0 0 74 74" aria-hidden="true">
    <path d="M6 70 H68 M12 70 V26 H62 V70 M24 26 V10 H50 V26 M37 13 V23 M32 18 H42 M20 36 H28 M34 36 H40 M46 36 H54 M20 48 H28 M34 48 H40 M46 48 H54 M32 70 V58 H42 V70"/>
  </svg>
  <svg class="deco" style="left:1140px;top:1010px" width="60" height="76" viewBox="0 0 68 76" aria-hidden="true">
    <path d="M14 6 V30 a14 14 0 0 0 28 0 V6 M28 44 V56 a12 12 0 0 0 24 0 V40 M52 40 a6 6 0 1 0 0.1 0"/>
  </svg>

  <ul class="features">
    <li class="feature">
      <svg viewBox="0 0 80 80" fill="none" stroke="var(--icon)" stroke-width="2.5" stroke-linejoin="round" stroke-linecap="round" aria-hidden="true">
        <rect x="4" y="6" width="72" height="50" rx="3"/><path d="M30 56 L28 68 H52 L50 56 M22 72 H58 M10 32 H22 L28 20 L36 42 L42 30 H48"/><path d="M58 24 c-3-4-9-2-8 3 c1 4 8 8 8 8 s7-4 8-8 c1-5-5-7-8-3 Z"/>
      </svg>
      <div>
        <h2 class="feature-title">Medical Check up</h2>
        <p class="feature-text">Social media can also be used<br>to share interesting facts</p>
      </div>
    </li>
    <li class="feature">
      <svg viewBox="0 0 80 80" fill="none" stroke="var(--icon)" stroke-width="2.5" stroke-linejoin="round" stroke-linecap="round" aria-hidden="true">
        <rect x="18" y="2" width="44" height="76" rx="4"/><path d="M18 12 H62 M18 66 H62 M30 44 H50 M30 50 H50 M30 56 H46"/><circle cx="40" cy="27" r="8"/><path d="M40 23 V31 M36 27 H44"/>
      </svg>
      <div>
        <h2 class="feature-title">Online Reservation</h2>
        <p class="feature-text">Social media can also be used<br>to share interesting facts</p>
      </div>
    </li>
    <li class="feature">
      <svg viewBox="0 0 80 80" fill="none" stroke="var(--icon)" stroke-width="2.5" stroke-linejoin="round" stroke-linecap="round" aria-hidden="true">
        <path d="M4 36 L40 10 L76 36 V76 H4 Z M4 36 L40 60 L76 36 M4 76 L32 54 M76 76 L48 54"/><rect x="20" y="4" width="40" height="40" fill="var(--white)"/><path d="M40 10 V22 M34 16 H46 M28 30 H52 M28 36 H52"/>
      </svg>
      <div>
        <h2 class="feature-title">Healthcare Report</h2>
        <p class="feature-text">Social media can also be used<br>to share interesting facts</p>
      </div>
    </li>
  </ul>

  <div class="book-btn">BOOK NOW <span aria-hidden="true">›</span></div>

  <div class="call">
    <svg viewBox="0 0 36 36" fill="none" stroke="var(--icon)" stroke-width="2.2" stroke-linejoin="round" stroke-linecap="round" aria-hidden="true">
      <path d="M8 4 L14 10 L10 15 C13 21 16 24 22 27 L27 23 L33 29 L28 34 C16 32 5 21 3 9 Z M20 4 a12 12 0 0 1 12 12 M20 10 a6 6 0 0 1 6 6"/>
    </svg>
    <div>
      <p class="call-label">Call For Appointment</p>
      <p class="call-number">123-555-0184</p>
    </div>
  </div>

  <p class="contact contact-email">
    <svg viewBox="0 0 30 24" fill="none" stroke="var(--white)" stroke-width="2" stroke-linejoin="round" aria-hidden="true"><rect x="2" y="3" width="26" height="18" rx="1"/><path d="M2 3 L15 14 L28 3"/></svg>
    hello@kovtahmclinic.com
  </p>
  <p class="contact contact-web">
    <svg viewBox="0 0 24 24" fill="none" stroke="var(--white)" stroke-width="2" aria-hidden="true"><circle cx="12" cy="12" r="10"/><ellipse cx="12" cy="12" rx="4" ry="10"/><path d="M2 12 H22"/></svg>
    www.kovtahmclinic.com
  </p>
</main>
</body>
</html>
```